Brookvale Holdings Ltd - Logo and Business Card

Create a logo and business card design for our new company.

Canadian private investment company with holdings in Saskatchewan Oil and real-estate.

Target Market(s)

Investors

Industry/Entity Type

Finance

Contact Information for Business Card

Name - Dominic Harlow
Position - President
Phone - 306.482.7159
Website - www.brookvaleholdings.ca

Logo Text

Today. Tomorrow. Together. (Tag Line)

Colors

Designer to choose colors to be used in the design.

Requirements
Must have
• Logo Must Have - Type Font only
• Must be modern, professional and stand out from the crowd.
Nice to have
• Don't have any, blank slate.

```html
<!DOCTYPE html>
<html lang="en">
<head>
<meta charset="utf-8">
<title>Brookvale Holdings Ltd – Business Card</title>
<link rel="stylesheet" href="https://fonts.googleapis.com/css2?family=Jost:wght@400&family=Source+Sans+3:wght@400;600&display=swap">
<style>
  :root {
    --stage-top: #2b2b2b;
    --stage-bottom: #050505;
    --card-white: #ffffff;
    --brand-blue: #1b75bb;
    --ink: #1a1a1a;
    --back-light: #1fb0e8;
    --back-mid: #1a9bd8;
    --back-deep: #0867a6;
    --on-blue: #ffffff;
  }
  * { margin: 0; padding: 0; box-sizing: border-box; }
  html, body { width: 1200px; height: 900px; overflow: hidden; }
  body {
    position: relative;
    background: linear-gradient(180deg, var(--stage-top) 0%, #161616 55%, var(--stage-bottom) 100%);
    font-family: "Source Sans 3", "Myriad Pro", sans-serif;
  }
  .card {
    position: absolute;
    top: 306px;
    width: 440px;
    height: 271px;
    border-radius: 12px;
    overflow: hidden;
  }
  .card--front { left: 149px; background: var(--card-white); }
  .card--back {
    left: 608px;
    background: linear-gradient(180deg, var(--back-light) 0%, var(--back-mid) 45%, var(--back-deep) 70%, var(--back-deep) 100%);
  }

  .brand-mark {
    position: absolute;
    border-radius: 50%;
  }
  .card--front .brand-mark {
    left: 86px; top: 68px; width: 74px; height: 74px;
    background: var(--brand-blue);
  }
  .card--back .brand-mark {
    left: 174px; top: 54px; width: 94px; height: 94px;
    background: var(--on-blue);
  }
  .brand-name {
    position: absolute;
    font-family: "Jost", "Futura", sans-serif;
    font-weight: 400;
    text-transform: uppercase;
    text-align: center;
    line-height: 1.02;
  }
  .brand-name span { display: block; }
  .card--front .brand-name {
    left: 20px; top: 148px; width: 208px;
    color: var(--brand-blue);
    font-size: 32px;
  }
  .card--front .brand-name .brand-name__sub { font-size: 22px; letter-spacing: 0.3px; }
  .card--back .brand-name {
    left: 60px; top: 150px; width: 320px;
    color: var(--on-blue);
    font-size: 38px;
  }
  .card--back .brand-name .brand-name__sub { font-size: 27px; letter-spacing: 0.5px; }

  .tagline {
    position: absolute;
    left: 60px; top: 226px; width: 320px;
    text-align: center;
    color: var(--on-blue);
    font-size: 13px;
    letter-spacing: 1px;
  }

  .contact {
    position: absolute;
    left: 244px; top: 64px;
    color: var(--ink);
    font-size: 12.5px;
    line-height: 15px;
  }
  .contact__name { color: var(--brand-blue); font-weight: 600; font-size: 15px; line-height: 18px; }
  .contact__role { margin-bottom: 23px; }
  .contact__address { margin-bottom: 13px; }
  .contact__list { list-style: none; }
  .contact__list li { display: flex; align-items: center; height: 16px; }
  .contact__list svg { width: 9px; height: 9px; margin-right: 7px; fill: var(--brand-blue); }
</style>
</head>
<body>

<section class="card card--front" aria-label="Business card front">
  <div class="brand-mark"></div>
  <div class="brand-name"><span>Brookvale</span><span class="brand-name__sub">Holdings Ltd</span></div>

  <div class="contact">
    <div class="contact__name">Dominic Harlow</div>
    <div class="contact__role">President</div>
    <div class="contact__address">2210 Albert Street<br>Regina, SK S4P 2V2.</div>
    <ul class="contact__list">
      <li><svg viewBox="0 0 10 10"><path d="M1 3 Q5 0 9 3 L8 4.5 L6.5 3.8 L6.5 3 Q5 2.5 3.5 3 L3.5 3.8 L2 4.5 Z M2.5 5 H7.5 L8.5 9 H1.5 Z"/></svg>306.482.7159</li>
      <li><svg viewBox="0 0 10 10"><path d="M0.5 2 H9.5 V8 H0.5 Z M1 2.5 L5 5.5 L9 2.5 V3.2 L5 6.2 L1 3.2 Z" fill-rule="evenodd"/></svg>info@brookvaleholdings.ca</li>
      <li><svg viewBox="0 0 10 10"><path d="M4 6 L6 4 M3.2 5 L1.8 6.4 A1.6 1.6 0 0 0 3.6 8.2 L5 6.8 M6.8 5 L8.2 3.6 A1.6 1.6 0 0 0 6.4 1.8 L5 3.2" stroke="var(--brand-blue)" stroke-width="1.3" fill="none"/></svg>www.brookvaleholdings.ca</li>
    </ul>
  </div>
</section>

<section class="card card--back" aria-label="Business card back">
  <div class="brand-mark"></div>
  <div class="brand-name"><span>Brookvale</span><span class="brand-name__sub">Holdings Ltd</span></div>
  <div class="tagline">Today. Tomorrow. Together.</div>
</section>

</body>
</html>
```